Healthy Food Healthy Brain Rack Card

We want a new 2 page (front and page) 3.67" x 8.5" rack card. This rack card is the first of a series we are creating. We will have five more eventually.

The minimum font size for the text on the front is 11 point and also for other main body text.

Use the text on the word document.

The images and layout in the word document are just sample ideas we had.

We have a subscripton to adobe stock images so prefer to get images from there or free high quality images.

The document is for older readers. Do not put text over graphics and keep it simple and easy to read with high contrast.

We are open to any color scheme, though something that conveys fresh and healthy, is good.

We want some very simple design element(s) incorporated that convey Native American communities or heritage. But NO head dress, teepee graphics, etc.

At the top, of the first page we would like a collage of healthy food images. This can include fish, chicken, fresh vegetables, berries, brown rice, etc.

On the back side, the text below the brown box on the word document with the title "mock up" can be smaller as needed.

Please remember to include the funding statement - it can be in a very small font 6/7 point.

For more information about our project, please visit https://velmorcollective.org/mind-care/

```html
<!DOCTYPE html>
<html lang="en">
<head>
<meta charset="utf-8">
<title>Healthy Food Healthy Brain Rack Card</title>
<link href="https://fonts.googleapis.com/css2?family=Archivo+Black&family=Archivo:wght@500;700;800&family=Roboto+Condensed:wght@400;700&display=swap" rel="stylesheet">
<style>
:root{
  --teal:#3fa6ad;
  --teal-dark:#1f7a78;
  --brown:#7a3324;
  --brick:#8b3a34;
  --red:#b5443d;
  --blush:#f8e9e6;
  --ink:#2a2a2a;
  --paper:#ffffff;
  --bg:#ececec;
}
*{box-sizing:border-box;margin:0;padding:0}
html,body{width:765px;height:1200px;overflow:hidden;background:var(--bg)}
body{position:relative;font-family:"Roboto Condensed",sans-serif;color:var(--ink)}
.card{position:absolute;top:195px;width:350px;height:810px;background:var(--paper);box-shadow:0 4px 14px rgba(0,0,0,.18);overflow:hidden}
.card--front{left:22px}
.card--back{left:393px}
.abs{position:absolute}
.rule-top{left:0;top:6px;width:350px;height:6px;background:var(--teal)}
.collage{left:0;top:14px}
.headline{left:0;top:280px;width:350px;text-align:center;font-family:"Archivo Black",sans-serif;font-size:18px;font-weight:400;letter-spacing:.2px;color:var(--brown)}
.headline .accent{color:var(--red)}
.headline .bar{color:var(--teal);font-family:"Archivo",sans-serif;font-weight:500}
.intro{left:36px;top:305px;width:278px;text-align:center;font-size:8.4px;line-height:11.5px}
.pill{background:var(--red);color:#fff;font-family:"Archivo",sans-serif;font-weight:700;text-align:center;border-radius:12px}
.steps-pill{left:36px;top:350px;width:278px;height:19px;line-height:19px;font-size:10.5px}
.tile{width:72px;height:70px;background:var(--brick);border-radius:4px;color:#fff;font-size:6.4px;line-height:8.6px;text-align:center;padding:26px 3px 0;box-shadow:0 2px 0 #5d231d}
.tile-tab{position:absolute;left:22px;top:-16px;width:28px;height:28px;background:var(--brick);border-radius:3px;border:1.5px solid #fff;display:flex;align-items:center;justify-content:center}
.closing{left:0;top:590px;width:350px;text-align:center;font-family:"Archivo",sans-serif;font-weight:700;font-size:10px;line-height:12px}
.quote-band{left:0;top:620px;width:350px;height:122px;background:var(--teal)}
.photo{position:absolute}
.quote-box{left:61px;top:630px;width:228px;height:102px;background:var(--blush);border-radius:14px;overflow:hidden;text-align:center}
.quote-head{background:var(--brick);color:#fff;font-family:"Archivo",sans-serif;font-weight:700;font-size:9.2px;line-height:11px;padding:6px 8px 7px;border-radius:14px 14px 0 0}
.quote-text{font-size:7px;line-height:9.5px;padding:9px 14px 0;position:relative}
.quote-mark{color:var(--red);font-weight:700;font-size:11px}
.quote-name{font-family:"Archivo",sans-serif;font-weight:700;color:var(--brown);font-size:9px;margin-top:6px}
.org{display:flex;align-items:center;gap:6px}
.org-dot{width:30px;height:30px;border-radius:50%;background:var(--teal);flex:none}
.org-name{font-family:"Archivo",sans-serif;font-weight:700;color:var(--teal);font-size:9.6px;line-height:10.5px;text-transform:uppercase}
.org--front{left:98px;top:752px}
/* back */
.back-head{left:0;top:19px;width:350px;height:42px;background:var(--teal);color:#fff;text-align:center;font-family:"Archivo",sans-serif;padding-top:5px}
.back-head h2{font-family:"Archivo Black",sans-serif;font-size:12.5px;line-height:15px;font-weight:400}
.back-head p{font-weight:700;font-size:9.2px;line-height:12px}
.frame{left:19px;top:76px;width:310px;height:249px;border:1px solid var(--brown)}
.ingr-pill{left:118px;top:68px;width:114px;height:18px;line-height:16px;font-size:10px;border:1.5px solid #fff;box-shadow:0 0 0 1px var(--brown)}
.ingr-photo{left:30px;top:98px;width:136px;height:214px;border-radius:4px}
.ingr-box{left:173px;top:97px;width:144px;height:216px;background:var(--brick);border-radius:12px;color:#fff;padding:16px 8px 0 9px;list-style:none;font-size:10px;line-height:17.5px}
.ingr-box li{display:flex;gap:4px;align-items:flex-start}
.ingr-box li svg{margin-top:4.5px;flex:none}
.method{left:19px;top:346px;width:304px;list-style:none;font-size:8px;line-height:11px}
.method li{display:flex;gap:6px;padding:5px 0;border-bottom:1px solid #f0cfcb}
.method li:last-child{border-bottom:none}
.method svg{flex:none;margin-top:1.5px}
.story-band{left:0;top:498px;width:350px;height:87px;background:var(--teal-dark)}
.story-text{left:34px;top:512px;width:196px;color:#fff;font-size:9.4px;line-height:13.5px}
.fruit-fall{left:240px;top:486px;width:96px;height:96px;border-radius:10px;background:radial-gradient(circle at 55% 45%,#f2c14b 0%,#d9452e 40%,#7da046 75%,rgba(31,122,120,0) 100%)}
.fruit-basket{left:174px;top:590px;width:158px;height:98px;border-radius:10px;background:linear-gradient(120deg,#9aa3a6 0%,#c9453a 35%,#e8b55a 55%,#8a5a2e 80%,#d8c29a 100%)}
.more{left:19px;top:597px;width:150px}
.more h3{font-family:"Archivo",sans-serif;font-weight:700;color:var(--red);font-size:9.6px;border-bottom:1.5px solid var(--red);padding-bottom:2px;margin-bottom:7px}
.more h4{font-family:"Archivo",sans-serif;font-weight:700;font-size:9.2px;line-height:11px;margin-top:6px}
.more .src{font-family:"Archivo",sans-serif;font-weight:700;color:var(--red);font-size:6.6px;line-height:8.2px}
.more .url{font-size:7px;line-height:10px;display:flex;gap:4px;align-items:center;text-decoration:underline;margin-top:2px;white-space:nowrap}
.url-dot{width:7px;height:7px;border-radius:50%;background:var(--red);flex:none}
.org-panel{left:169px;top:693px;width:160px;height:44px;background:var(--blush);padding-left:10px}
.funding{left:32px;top:752px;width:286px;text-align:center;font-size:5.4px;line-height:7.2px}
.rule-bottom{left:0;top:792px;width:350px;height:18px;background:var(--teal)}
</style>
</head>
<body>

<section class="card card--front">
  <div class="abs rule-top"></div>
  <svg class="abs collage" width="350" height="262" viewBox="0 0 350 262">
    <defs>
      <linearGradient id="gSalmon" x1="0" y1="0" x2="1" y2="1"><stop offset="0" stop-color="#e9e6e2"/><stop offset=".5" stop-color="#b86a45"/><stop offset="1" stop-color="#3c5a2a"/></linearGradient>
      <linearGradient id="gProtein" x1="0" y1="0" x2="1" y2="0"><stop offset="0" stop-color="#f0a187"/><stop offset=".5" stop-color="#a5463f"/><stop offset="1" stop-color="#e9c7a0"/></linearGradient>
      <linearGradient id="gVeg" x1="0" y1="0" x2="1" y2="0"><stop offset="0" stop-color="#7a2d3a"/><stop offset=".4" stop-color="#4f7d3a"/><stop offset=".7" stop-color="#e8a32a"/><stop offset="1" stop-color="#d24a2c"/></linearGradient>
      <radialGradient id="gBerry" cx=".55" cy=".55" r=".6"><stop offset="0" stop-color="#e1332d"/><stop offset=".8" stop-color="#c6282a"/><stop offset="1" stop-color="#f4f0ee"/></radialGradient>
    </defs>
    <polygon points="0,0 162,0 176,120 0,120" fill="url(#gSalmon)" role="img" aria-label="Photo of grilled salmon fillet on spinach with lemon"/>
    <polygon points="162,0 171,0 185,120 176,120" fill="var(--teal)"/>
    <polygon points="171,0 350,0 350,120 185,120" fill="url(#gProtein)" role="img" aria-label="Photo of raw salmon, fish, red meat, chicken and eggs on a board"/>
    <rect x="0" y="120" width="350" height="10" fill="var(--teal)"/>
    <polygon points="0,131 194,131 166,252 0,252" fill="url(#gVeg)" role="img" aria-label="Photo of assorted fresh vegetables"/>
    <polygon points="194,131 204,131 176,252 166,252" fill="var(--teal)"/>
    <polygon points="204,131 350,131 350,252 176,252" fill="url(#gBerry)" role="img" aria-label="Photo of fresh strawberries"/>
    <rect x="0" y="253" width="350" height="9" fill="var(--teal)"/>
  </svg>

  <h1 class="abs headline">HEALTHY FOOD <span class="bar">|</span> <span class="accent">HEALTHY BRAIN</span></h1>
  <p class="abs intro">Everyone slows down as they get older, both in body and mind. Eating healthier food can help your overall health, including brain health. It may also reduce your risk for memory loss and problems thinking.</p>
  <div class="abs pill steps-pill">HEALTHIER STEPS TO PROTECT YOUR BRAIN:</div>

  <div class="abs tile" style="left:20px;top:402px"><span class="tile-tab"><svg width="16" height="16" viewBox="0 0 16 16" fill="none" stroke="#fff" stroke-width="1.2"><circle cx="6" cy="9" r="4"/><circle cx="10.5" cy="8" r="3.5"/><path d="M8 4 L9 1.5"/></svg></span>Eat more vegetables, fruits, whole grains, and lower-fat milk</div>
  <div class="abs tile" style="left:99px;top:402px"><span class="tile-tab"><svg width="16" height="16" viewBox="0 0 16 16" fill="none" stroke="#fff" stroke-width="1.2"><rect x="3" y="5" width="6" height="9" rx="1"/><rect x="3.5" y="2" width="5" height="3"/><circle cx="12.5" cy="11" r="1"/></svg></span>Use less salt and added sugar</div>
  <div class="abs tile" style="left:177px;top:402px"><span class="tile-tab"><svg width="16" height="16" viewBox="0 0 16 16" fill="none" stroke="#fff" stroke-width="1.2"><path d="M2 8 C5 3 11 3 13 8 C11 13 5 13 2 8 Z"/><path d="M13 8 L15 5 L15 11 Z"/></svg></span>Eat more fish, chicken, turkey, beans, and nuts</div>
  <div class="abs tile" style="left:256px;top:402px"><span class="tile-tab"><svg width="16" height="16" viewBox="0 0 16 16" fill="none" stroke="#fff" stroke-width="1.2"><circle cx="8" cy="8" r="6.5"/><circle cx="8" cy="8" r="3.5"/></svg></span>Cut down on bad fats ("saturated" and trans), cholesterol, and red meat</div>

  <div class="abs tile" style="left:20px;top:505px"><span class="tile-tab"><svg width="16" height="16" viewBox="0 0 16 16" fill="none" stroke="#fff" stroke-width="1.2"><path d="M2 7 H14 L12.5 14 H3.5 Z"/><circle cx="6" cy="4.5" r="1.5"/><circle cx="10" cy="4.5" r="1.5"/></svg></span>Buy fresh, not packaged food when you can</div>
  <div class="abs tile" style="left:99px;top:505px"><span class="tile-tab"><svg width="16" height="16" viewBox="0 0 16 16" fill="none" stroke="#fff" stroke-width="1.2"><rect x="5.5" y="6" width="5" height="8.5" rx="1"/><path d="M7 6 V2 H9 V6"/></svg></span>Limit how much alcohol you drink</div>
  <div class="abs tile" style="left:177px;top:505px"><span class="tile-tab"><svg width="16" height="16" viewBox="0 0 16 16" fill="none" stroke="#fff" stroke-width="1.2"><path d="M8 2 C4 6 3.5 9 4 11 C5 14 11 14 12 11 C12.5 9 11 6 8 2 Z"/></svg></span>Learn your daily calorie needs for your body size</div>
  <div class="abs tile" style="left:256px;top:505px"><span class="tile-tab"><svg width="16" height="16" viewBox="0 0 16 16" fill="none" stroke="#fff" stroke-width="1.2"><circle cx="6" cy="7" r="4"/><circle cx="10" cy="7" r="4"/><path d="M6 11 V14 M10 11 V14"/></svg></span>Take care of your mental and spiritual health to support your physical and brain health</div>

  <p class="abs closing">SMALL CHANGES CAN MAKE A BIG DIFFERENCE<br>FOR BETTER BRAIN HEALTH.</p>

  <div class="abs quote-band">
    <div class="photo" role="img" aria-label="Photo of a salmon fillet on a plate" style="left:0;top:18px;width:60px;height:74px;border-radius:0 40px 40px 0;background:linear-gradient(135deg,#f4b08a,#e7673f)"></div>
    <div class="photo" role="img" aria-label="Photo of raw salmon slice" style="left:296px;top:10px;width:54px;height:44px;border-radius:20px 0 0 20px;background:linear-gradient(135deg,#f6c2a8,#ee7a52)"></div>
    <div class="photo" role="img" aria-label="Photo of a bowl of brown rice" style="left:292px;top:70px;width:58px;height:52px;border-radius:30px 0 0 0;background:radial-gradient(circle at 60% 60%,#e3c9a0,#b98a58)"></div>
  </div>
  <div class="abs quote-box">
    <div class="quote-head">TALK TO YOUR DOCTOR ABOUT MORE<br>STEPS TO HEALTHIER FOOD CHOICES.</div>
    <p class="quote-text"><span class="quote-mark">“</span> Without the elk, salmon, huckleberries, shellfish, and cedar trees we are nobody… <span class="quote-mark">”</span></p>
    <p class="quote-name">Lorna Whitefeather <span style="font-weight:500">(Cedar River)</span></p>
  </div>

  <div class="abs org org--front"><span class="org-dot"></span><span class="org-name">Velmor Collective<br>Resource Center for Mind Care</span></div>
</section>

<section class="card card--back">
  <header class="abs back-head">
    <h2>MAKE THIS AT HOME</h2>
    <p>GRILLED SALMON AND VEGGIE FOIL PACKETS</p>
  </header>
  <div class="abs frame"></div>
  <div class="abs pill ingr-pill">INGREDIENTS:</div>
  <div class="abs ingr-photo" role="img" aria-label="Photos of red and green chili peppers, sliced raw salmon and asparagus" style="background:linear-gradient(180deg,#d83a2c 0%,#7ca142 28%,#f5925c 45%,#f07a45 60%,#8fb25a 80%,#f7f7f5 100%)"></div>
  <ul class="abs ingr-box">
    <li><svg width="8" height="8" viewBox="0 0 8 8"><circle cx="4" cy="4" r="4" fill="#fff"/><path d="M2 4.2 L3.4 5.5 L6 2.7" stroke="#8b3a34" stroke-width="1.1" fill="none"/></svg>Salmon</li>
    <li><svg width="8" height="8" viewBox="0 0 8 8"><circle cx="4" cy="4" r="4" fill="#fff"/><path d="M2 4.2 L3.4 5.5 L6 2.7" stroke="#8b3a34" stroke-width="1.1" fill="none"/></svg>Asparagus</li>
    <li><svg width="8" height="8" viewBox="0 0 8 8"><circle cx="4" cy="4" r="4" fill="#fff"/><path d="M2 4.2 L3.4 5.5 L6 2.7" stroke="#8b3a34" stroke-width="1.1" fill="none"/></svg><span>Red or Green Peppers<br>(Or any seasonal vegetable)</span></li>
    <li><svg width="8" height="8" viewBox="0 0 8 8"><circle cx="4" cy="4" r="4" fill="#fff"/><path d="M2 4.2 L3.4 5.5 L6 2.7" stroke="#8b3a34" stroke-width="1.1" fill="none"/></svg>Onion</li>
    <li><svg width="8" height="8" viewBox="0 0 8 8"><circle cx="4" cy="4" r="4" fill="#fff"/><path d="M2 4.2 L3.4 5.5 L6 2.7" stroke="#8b3a34" stroke-width="1.1" fill="none"/></svg>Lemon – sliced</li>
    <li><svg width="8" height="8" viewBox="0 0 8 8"><circle cx="4" cy="4" r="4" fill="#fff"/><path d="M2 4.2 L3.4 5.5 L6 2.7" stroke="#8b3a34" stroke-width="1.1" fill="none"/></svg>Basil</li>
    <li><svg width="8" height="8" viewBox="0 0 8 8"><circle cx="4" cy="4" r="4" fill="#fff"/><path d="M2 4.2 L3.4 5.5 L6 2.7" stroke="#8b3a34" stroke-width="1.1" fill="none"/></svg>Olive Oil</li>
    <li><svg width="8" height="8" viewBox="0 0 8 8"><circle cx="4" cy="4" r="4" fill="#fff"/><path d="M2 4.2 L3.4 5.5 L6 2.7" stroke="#8b3a34" stroke-width="1.1" fill="none"/></svg>Salt and Pepper</li>
    <li><svg width="8" height="8" viewBox="0 0 8 8"><circle cx="4" cy="4" r="4" fill="#fff"/><path d="M2 4.2 L3.4 5.5 L6 2.7" stroke="#8b3a34" stroke-width="1.1" fill="none"/></svg>Garlic Powder</li>
  </ul>

  <ol class="abs method">
    <li><svg width="8" height="8" viewBox="0 0 8 8"><circle cx="4" cy="4" r="4" fill="#3fa6ad"/><path d="M2 4.2 L3.4 5.5 L6 2.7" stroke="#fff" stroke-width="1.1" fill="none"/></svg>Cut asparagus, peppers, and onion into bite-size pieces.</li>
    <li><svg width="8" height="8" viewBox="0 0 8 8"><circle cx="4" cy="4" r="4" fill="#3fa6ad"/><path d="M2 4.2 L3.4 5.5 L6 2.7" stroke="#fff" stroke-width="1.1" fill="none"/></svg>Cut salmon into 4-6 oz pieces. Tear tin foil large enough to wrap around salmon &amp; veggies (2 layers).</li>
    <li><svg width="8" height="8" viewBox="0 0 8 8"><circle cx="4" cy="4" r="4" fill="#3fa6ad"/><path d="M2 4.2 L3.4 5.5 L6 2.7" stroke="#fff" stroke-width="1.1" fill="none"/></svg>Add veggies and salmon to foil. Drizzle with olive oil, season with salt, pepper, basil, garlic &amp; top with a piece of sliced lemon.</li>
    <li><svg width="8" height="8" viewBox="0 0 8 8"><circle cx="4" cy="4" r="4" fill="#3fa6ad"/><path d="M2 4.2 L3.4 5.5 L6 2.7" stroke="#fff" stroke-width="1.1" fill="none"/></svg>Wrap foil tightly around food. Grill at 400 degrees for about 20 minutes. Careful opening!</li>
  </ol>

  <div class="abs story-band"></div>
  <p class="abs story-text">Food &amp; drink are a source of strength and connection to community. A return to traditional food pathways and eating local, seasonal fresh foods make healthier eating easier.</p>
  <div class="abs photo fruit-fall" role="img" aria-label="Photo of fresh fruits and vegetables falling"></div>
  <div class="abs photo fruit-basket" role="img" aria-label="Photo of a heart-shaped bowl of produce, a basket of fruit and a scoop of grains"></div>

  <div class="abs more">
    <h3>FOR MORE INFORMATION</h3>
    <h4>ABOUT HEALTHIER EATING</h4>
    <p class="src">PlateWise</p>
    <p class="url"><span class="url-dot"></span>https://www.platewise.org</p>
    <h4>ABOUT BRAIN HEALTH</h4>
    <p class="src">Velmor Collective Resource Center<br>for Mind Care</p>
    <p class="url"><span class="url-dot"></span>https://www.velmorcollective.org/mind-care/</p>
    <p class="src" style="margin-top:8px">Northfield Memory Program</p>
    <p class="url"><span class="url-dot"></span>https://www.northfieldmemory.org/aging</p>
  </div>

  <div class="abs org org-panel"><span class="org-dot"></span><span class="org-name">Velmor Collective<br>Resource Center for Mind Care</span></div>

  <p class="abs funding">This product is supported by the Northfield Health Foundation (NHF) as part of a financial assistance award totaling $348,711 with 100 percent funded by NHF. The contents are those of the author(s) and do not necessarily represent the official views of, nor an endorsement, by NHF or the Foundation's partners.</p>
  <div class="abs rule-bottom"></div>
</section>

</body>
</html>
```